International Automotive Parts Marketing business needs professional, sleek Android app design.

We have developed an Android app for our sales team and are now looking for an overall design our developers can apply. The design should mirror our corporate website kvrl.com. There is a LOT of data the reps need to work through so not really any images other that login screen - of course icons are great. Lots of lists and searches etc. - it needs to look professional, feel amazing and easy to use. Our motto - Simple is always better. We included our logo and a few screenshots of the app page 1 and 2.

Target Market(s)

Professional Sales and Marketing - our own sales team (100 reps) will use this app

Font styles to use
Sans Serif

Colors

Designer to choose colors to be used in the design.

Requirements
Must have
• App design must be professional and easy to use in the field all day. Similar look and feel of corporate website kvrl.com. Same colors and images. Icons to manage navigation
Should not have
• Non-professional look and feel. No vector cartoon type images. No specific parts related images

```html
<!DOCTYPE html>
<html lang="en">
<head>
<meta charset="utf-8">
<title>Kevral Parts Group – Sales App Screens</title>
<link href="https://fonts.googleapis.com/css2?family=Roboto:wght@300;400;500;700&display=swap" rel="stylesheet">
<style>
:root{
  --canvas:#e6e6e6;
  --black:#000;
  --red:#d0112b;
  --white:#fff;
  --paper:#f3f3f3;
  --ink:#222;
  --muted:#8f8f8f;
  --line:#dcdcdc;
  --soft:#ececec;
}
*{box-sizing:border-box;margin:0;padding:0}
html,body{width:1200px;height:865px;overflow:hidden;background:var(--canvas);font-family:'Roboto',sans-serif;color:var(--ink)}
.screen{position:absolute;width:313px;transform:scale(.529);transform-origin:0 0;background:var(--paper);overflow:hidden;box-shadow:0 20px 40px rgba(0,0,0,.12)}
.a{position:absolute}
.status{position:absolute;left:0;top:0;width:100%;height:22px;background:var(--black);color:var(--white);font-size:12px;text-align:right;padding:4px 8px 0 0}
.status svg{vertical-align:-1px;margin-right:3px}
.appbar{position:absolute;left:0;top:22px;width:100%;height:48px;background:var(--black);color:var(--white)}
.appbar .title{position:absolute;left:62px;top:14px;font-size:17px;font-weight:500}
.appbar .nav{position:absolute;left:16px;top:14px}
.appbar .act{position:absolute;right:12px;top:14px}
.card{position:absolute;background:var(--white)}
.lbl{font-size:10px;color:var(--muted)}
.val{font-size:13px;color:var(--ink)}
.field-line{border-bottom:1px solid var(--line)}
.btn-red{position:absolute;background:var(--red);color:var(--white);font-size:12px;font-weight:500;text-align:center;border-radius:2px}
.chk{position:absolute;width:16px;height:16px;border:2px solid #777;border-radius:2px}
.chk.on{background:var(--red);border-color:var(--red)}
.brand{display:flex;align-items:center;gap:8px;font-weight:700;letter-spacing:1px}
.brand .dot{width:44px;height:44px;border-radius:50%}
.co-row .name{font-size:13px;font-weight:500}
.co-row .sub{font-size:11px;color:var(--muted)}
.co-row .meta{font-size:11px;color:var(--muted)}
.co-row .meta b{color:var(--ink);font-weight:400}
.avatar{position:absolute;width:36px;height:36px;border-radius:50%;background:#eee;color:#c9c9c9;font-size:18px;font-weight:500;text-align:center;line-height:36px}
</style>
</head>
<body>

<!-- Login -->
<section class="screen login" style="left:73px;top:84px;height:627px;background:#111">
  <div class="a" role="img" aria-label="Dark red sports truck photographed in a showroom" style="left:0;top:0;width:313px;height:627px;background:linear-gradient(180deg,#2a2a2c 0%,#3a1a1c 28%,#7a0f17 45%,#4a0c10 62%,#141414 82%,#0c0c0c 100%)"></div>
  <div class="a brand" style="left:42px;top:212px;color:var(--white);font-size:22px">
    <span class="dot" style="background:var(--white);width:52px;height:52px"></span>
    <span style="line-height:1">KEVRAL<br><span style="font-size:10px;letter-spacing:3px;font-weight:700">PARTS GROUP</span></span>
  </div>
  <div class="a" style="left:37px;top:374px;width:245px;height:37px;background:rgba(60,60,60,.55);border-radius:3px;color:#aaa;font-size:13px;text-align:center;line-height:37px">Username</div>
  <div class="a" style="left:37px;top:418px;width:245px;height:37px;background:rgba(60,60,60,.55);border-radius:3px;color:#aaa;font-size:13px;text-align:center;line-height:37px">Password</div>
  <div class="btn-red" style="left:37px;top:465px;width:243px;height:30px;line-height:30px">SIGN IN</div>
  <div class="a" style="left:0;top:507px;width:313px;text-align:center;color:#bbb;font-size:13px">Forgot password?</div>
  <div class="a" style="left:0;top:594px;width:313px;text-align:center;color:#aaa;font-size:13px">New User? Sign up <span style="color:var(--white)">here</span> <span style="color:var(--red)">›</span></div>
</section>

<!-- Navigation drawer -->
<section class="screen drawer" style="left:308px;top:88px;height:622px;background:#d7d7d7">
  <div class="status">
    <svg width="30" height="11" viewBox="0 0 30 11"><path d="M0 2 L7 10 L14 2 Q7 -2 0 2Z M16 10 L24 10 L24 2Z" fill="#fff"/><rect x="26" y="1" width="4" height="9" fill="#fff"/></svg>12:30
  </div>
  <div class="a" style="left:267px;top:22px;width:46px;height:48px;background:var(--black)"></div>
  <div class="a" style="left:267px;top:70px;width:30px;height:552px;background:#c9c9c9"></div>
  <div class="a" style="left:0;top:0;width:267px;height:622px;background:var(--white)">
    <div class="a" role="img" aria-label="Red truck headlight close-up" style="left:0;top:22px;width:267px;height:151px;background:linear-gradient(135deg,#5a0a10 0%,#b0121f 45%,#6a0c12 100%)"></div>
    <div class="a" style="left:20px;top:126px;width:34px;height:34px;border-radius:50%;background:#555"></div>
    <div class="a" style="left:64px;top:122px;color:var(--white);font-size:13px">JaneOrlov</div>
    <div class="a" style="left:64px;top:141px;color:#e6e6e6;font-size:13px">JaneOrlov@kvrl.com</div>
    <div class="a" style="left:242px;top:122px;color:var(--white);font-size:14px">›</div>
    <div class="a" style="left:6px;top:228px;width:254px;height:32px;background:#efefef"></div>
    <div class="a" style="left:30px;top:200px;font-size:13px;line-height:37.3px;color:#999">
      <div>⊤</div><div style="color:var(--red)">⌕</div><div>≡</div><div>∞</div><div>▣</div><div>⚙</div>
    </div>
    <div class="a" style="left:64px;top:200px;font-size:13.5px;line-height:37.3px">
      <div>Route</div><div>Search</div><div>Custom list</div><div>Partners</div><div>Market touches</div><div>Settings</div>
    </div>
    <div class="a brand" style="left:26px;top:517px;color:#1a1a1a;font-size:20px">
      <span class="dot" style="background:var(--red);width:50px;height:50px"></span>
      <span style="line-height:1">KEVRAL<br><span style="font-size:9px;letter-spacing:3px">PARTS GROUP</span></span>
    </div>
    <div class="a" style="left:0;top:596px;width:267px;border-top:1px solid var(--line)"></div>
    <div class="a" style="left:22px;top:603px;font-size:7px;color:#aaa">All rights reserved</div>
    <div class="a" style="left:177px;top:603px;font-size:7px;color:#aaa">Copyright 2020</div>
  </div>
</section>

<!-- Search -->
<section class="screen search" style="left:540px;top:93px;height:940px">
  <div class="status">12:30</div>
  <div class="appbar">
    <svg class="nav" width="18" height="14" viewBox="0 0 18 14"><path d="M0 1h18M0 7h18M0 13h18" stroke="#fff" stroke-width="2"/></svg>
    <div class="title">Search</div>
  </div>
  <div class="card" style="left:7px;top:82px;width:298px;height:700px">
    <div class="a lbl" style="left:7px;top:16px">Enter keyword</div>
    <div class="a val field-line" style="left:7px;top:32px;width:285px;padding-bottom:6px;border-color:#333">Engine<span style="color:var(--red)">|</span></div>
    <div class="a lbl" style="right:6px;top:64px">31 / 50</div>
    <div class="a val field-line" style="left:7px;top:96px;width:128px;padding-bottom:6px">Type <span style="float:right;color:#777">⌄</span></div>
    <div class="a val field-line" style="left:164px;top:96px;width:128px;padding-bottom:6px">Rating <span style="float:right;color:#777">⌄</span></div>
    <div class="a val" style="left:9px;top:164px;width:283px">More options <span style="float:right">︿</span></div>
    <div class="a lbl" style="left:7px;top:208px">Market</div>
    <div class="a val field-line" style="left:7px;top:226px;width:285px;padding-bottom:6px">All <span style="float:right;font-size:9px;color:#666">▼</span></div>
    <div class="a lbl" style="left:7px;top:277px">Franchise</div>
    <div class="a val field-line" style="left:7px;top:294px;width:285px;padding-bottom:6px">All <span style="float:right;font-size:9px;color:#666">▼</span></div>
    <div class="a lbl" style="left:7px;top:345px">LOI</div>
    <div class="a val field-line" style="left:7px;top:362px;width:285px;padding-bottom:6px">All <span style="float:right;font-size:9px;color:#666">▼</span></div>
    <div class="chk" style="left:10px;top:430px;border-color:#bbb"></div>
    <div class="a val" style="left:36px;top:430px">Rewards</div>
    <div class="chk on" style="left:154px;top:430px"><svg width="12" height="12" viewBox="0 0 12 12"><path d="M2 6l3 3 5-6" stroke="#fff" stroke-width="2" fill="none"/></svg></div>
    <div class="a val" style="left:180px;top:429px">My touches</div>
    <div class="a val field-line" style="left:7px;top:478px;width:285px;padding-bottom:7px">Touch start</div>
    <div class="a val field-line" style="left:7px;top:551px;width:285px;padding-bottom:7px">Touch end</div>
    <div class="a val field-line" style="left:7px;top:618px;width:285px;padding-bottom:7px">Sales type</div>
    <div class="btn-red" style="left:7px;top:663px;width:285px;height:30px;line-height:30px">SEARCH</div>
  </div>
  <div class="card" style="left:7px;top:794px;width:298px;height:56px">
    <div class="a" style="left:12px;top:11px;width:34px;height:34px;border-radius:50%;background:#fde8eb"></div>
    <svg class="a" style="left:20px;top:20px" width="18" height="14" viewBox="0 0 18 14"><circle cx="6" cy="4" r="3" fill="var(--red)"/><path d="M0 13c0-4 12-4 12 0z" fill="var(--red)"/><circle cx="13" cy="4" r="2.5" fill="var(--red)"/></svg>
    <div class="a val" style="left:53px;top:20px">My Clients</div>
    <div class="a" style="right:16px;top:16px;font-size:18px">›</div>
  </div>
  <div class="card" style="left:7px;top:857px;width:298px;height:56px">
    <div class="a" style="left:12px;top:11px;width:34px;height:34px;border-radius:50%;background:#fde8eb"></div>
    <svg class="a" style="left:21px;top:20px" width="16" height="14" viewBox="0 0 16 14"><rect x="0" y="3" width="16" height="11" rx="1" fill="var(--red)"/><rect x="5" y="0" width="6" height="4" fill="none" stroke="var(--red)" stroke-width="1.5"/></svg>
    <div class="a val" style="left:53px;top:19px">Add Company</div>
    <div class="a" style="right:16px;top:16px;font-size:18px">›</div>
  </div>
</section>

<!-- Company list -->
<section class="screen list" style="left:751px;top:92px;height:690px">
  <div class="status">12:30</div>
  <div class="appbar">
    <div class="nav" style="position:absolute;left:16px;top:10px;font-size:18px">←</div>
    <div class="title">Company List</div>
    <svg class="act" width="16" height="16" viewBox="0 0 16 16"><circle cx="6.5" cy="6.5" r="5" stroke="#999" stroke-width="1.6" fill="none"/><path d="M10 10l5 5" stroke="#999" stroke-width="1.6"/></svg>
  </div>
  <div class="a lbl" style="left:169px;top:81px;font-size:11px">Group By</div>
  <div class="a" style="left:225px;top:77px;width:70px;height:20px;border-radius:10px;background:#e2e2e2;font-size:11px;padding:3px 0 0 14px">None <span style="font-size:8px;margin-left:8px">▼</span></div>
  <div class="a" style="left:7px;top:103px;width:298px">
    <!-- seven rows -->
    <div class="card co-row" style="position:relative;height:76px;margin-bottom:6px"><div class="avatar" style="left:6px;top:20px">AC</div><div class="a name" style="left:56px;top:13px">214 Motor Works</div><div class="a sub" style="left:56px;top:31px">Fort Lindell, BC</div><div class="a meta" style="left:56px;top:48px">Type&nbsp; <b>M</b>&nbsp;&nbsp;&nbsp; Rating <b>B</b>&nbsp;&nbsp;&nbsp; Last touch&nbsp; <b>29 Oct, 2019</b></div><div class="a" style="right:12px;top:6px;color:var(--red)">›</div></div>
    <div class="card co-row" style="position:relative;height:76px;margin-bottom:6px"><div class="avatar" style="left:6px;top:20px">AC</div><div class="a name" style="left:56px;top:13px">214 Motor Works</div><div class="a sub" style="left:56px;top:31px">Fort Lindell, BC</div><div class="a meta" style="left:56px;top:48px">Type&nbsp; <b>M</b>&nbsp;&nbsp;&nbsp; Rating <b>B</b>&nbsp;&nbsp;&nbsp; Last touch&nbsp; <b>29 Oct, 2019</b></div><div class="a" style="right:12px;top:6px;color:var(--red)">›</div></div>
    <div class="card co-row" style="position:relative;height:76px;margin-bottom:6px"><div class="avatar" style="left:6px;top:20px">AC</div><div class="a name" style="left:56px;top:13px">214 Motor Works</div><div class="a sub" style="left:56px;top:31px">Fort Lindell, BC</div><div class="a meta" style="left:56px;top:48px">Type&nbsp; <b>M</b>&nbsp;&nbsp;&nbsp; Rating <b>B</b>&nbsp;&nbsp;&nbsp; Last touch&nbsp; <b>29 Oct, 2019</b></div><div class="a" style="right:12px;top:6px;color:var(--red)">›</div></div>
    <div class="card co-row" style="position:relative;height:76px;margin-bottom:6px"><div class="avatar" style="left:6px;top:20px">AC</div><div class="a name" style="left:56px;top:13px">214 Motor Works</div><div class="a sub" style="left:56px;top:31px">Fort Lindell, BC</div><div class="a meta" style="left:56px;top:48px">Type&nbsp; <b>M</b>&nbsp;&nbsp;&nbsp; Rating <b>B</b>&nbsp;&nbsp;&nbsp; Last touch&nbsp; <b>29 Oct, 2019</b></div><div class="a" style="right:12px;top:6px;color:var(--red)">›</div></div>
    <div class="card co-row" style="position:relative;height:76px;margin-bottom:6px"><div class="avatar" style="left:6px;top:20px">AC</div><div class="a name" style="left:56px;top:13px">214 Motor Works</div><div class="a sub" style="left:56px;top:31px">Fort Lindell, BC</div><div class="a meta" style="left:56px;top:48px">Type&nbsp; <b>M</b>&nbsp;&nbsp;&nbsp; Rating <b>B</b>&nbsp;&nbsp;&nbsp; Last touch&nbsp; <b>29 Oct, 2019</b></div><div class="a" style="right:12px;top:6px;color:var(--red)">›</div></div>
    <div class="card co-row" style="position:relative;height:76px;margin-bottom:6px"><div class="avatar" style="left:6px;top:20px">AC</div><div class="a name" style="left:56px;top:13px">214 Motor Works</div><div class="a sub" style="left:56px;top:31px">Fort Lindell, BC</div><div class="a meta" style="left:56px;top:48px">Type&nbsp; <b>M</b>&nbsp;&nbsp;&nbsp; Rating <b>B</b>&nbsp;&nbsp;&nbsp; Last touch&nbsp; <b>29 Oct, 2019</b></div><div class="a" style="right:12px;top:6px;color:var(--red)">›</div></div>
    <div class="card co-row" style="position:relative;height:76px"><div class="avatar" style="left:6px;top:20px">AC</div><div class="a name" style="left:56px;top:13px">214 Motor Works</div><div class="a sub" style="left:56px;top:31px">Fort Lindell, BC</div><div class="a meta" style="left:56px;top:48px">Type&nbsp; <b>M</b>&nbsp;&nbsp;&nbsp; Rating <b>B</b>&nbsp;&nbsp;&nbsp; Last touch&nbsp; <b>29 Oct, 2019</b></div><div class="a" style="right:12px;top:6px;color:var(--red)">›</div></div>
  </div>
</section>

<!-- Company detail -->
<section class="screen detail" style="left:968px;top:93px;height:594px">
  <div class="status">12:30</div>
  <div class="a" style="left:0;top:22px;width:313px;height:111px;background:var(--black);color:var(--white)">
    <div class="a" style="left:16px;top:12px;font-size:18px">←</div>
    <div class="a" style="left:51px;top:14px;font-size:20px;font-weight:500;line-height:23px">214<br>Motor Works</div>
    <div class="a" style="left:51px;top:67px;font-size:11px;color:#ccc;line-height:19px">⚲ Fort Lindell, BC<br>&nbsp;&nbsp;&nbsp;Canda V2x 4p1</div>
  </div>
  <div class="card" style="left:7px;top:140px;width:298px;height:340px">
    <div class="a" style="left:40px;top:34px;font-size:11px;line-height:21.3px;color:var(--muted)">Address<br>Phone<br>Fax<br>Email</div>
    <div class="a" style="left:139px;top:34px;font-size:11px;line-height:21.3px">412 B, Cedar Road<br>60455012<br>60455012<br>info@214motor.com</div>
    <div class="a" style="left:40px;top:129px;width:214px;border-top:1px solid var(--line)"></div>
    <div class="a" style="left:40px;top:143px;font-size:11px;line-height:22px;color:var(--muted)">Comment<br>Type<br>Rating</div>
    <div class="a" style="left:139px;top:143px;font-size:11px;line-height:22px">-<br>M<br>B</div>
    <div class="a" style="left:40px;top:222px;width:214px;border-top:1px solid var(--line)"></div>
    <div class="a" style="left:40px;top:237px;font-size:11px;color:var(--muted)">Partner</div>
    <div class="a" style="left:139px;top:237px;font-size:11px">Halden Motors</div>
    <div class="a" style="left:0;top:298px;width:298px;border-top:1px solid var(--line)"></div>
    <svg class="a" style="left:16px;top:310px" width="16" height="16" viewBox="0 0 16 16"><path d="M2 14l2-5 8-8 3 3-8 8z" fill="var(--red)"/></svg>
    <div class="a val" style="left:45px;top:310px">Edit</div>
    <div class="a" style="left:187px;top:309px;color:#999;font-size:14px">≡</div>
    <div class="a val" style="left:215px;top:310px">Modify list</div>
  </div>
</section>

<!-- Choose dialog -->
<section class="screen dialog" style="left:73px;top:466px;height:593px;background:#a9a9a9">
  <div class="status">12:30</div>
  <div class="a" style="left:0;top:22px;width:313px;height:110px;background:var(--black);color:var(--white)">
    <svg class="a" style="left:16px;top:18px" width="16" height="12" viewBox="0 0 16 12"><path d="M0 1h16M0 6h16M0 11h16" stroke="#bbb" stroke-width="1.6"/></svg>
    <div class="a" style="left:51px;top:14px;font-size:20px;font-weight:500;line-height:23px">214<br>Motor Works</div>
    <div class="a" style="left:51px;top:66px;font-size:11px;color:#ccc;line-height:19px">⚲ Fort Lindell, BC<br>&nbsp;&nbsp;&nbsp;Canda V2x 4p1</div>
  </div>
  <div class="a" style="left:8px;top:140px;width:298px;height:460px;background:#b4b4b4"></div>
  <div class="card" style="left:15px;top:170px;width:282px;height:316px;border-radius:2px;box-shadow:0 6px 18px rgba(0,0,0,.25)">
    <div class="a" style="left:31px;top:34px;font-size:16px;font-weight:500">Choose One</div>
    <div class="a" style="left:31px;top:74px;font-size:13.5px;line-height:45.5px;color:#444">Contacts<br>Touches<br>Alerts<br>Rewards<br>Supplier</div>
    <div class="a" style="right:25px;top:280px;font-size:13px;color:#888">CANCEL</div>
  </div>
</section>

<!-- Shop suppliers -->
<section class="screen suppliers" style="left:307px;top:460px;height:648px">
  <div class="status">12:30</div>
  <div class="appbar">
    <div class="nav" style="position:absolute;left:16px;top:10px;font-size:18px">←</div>
    <div class="title">Shop Suppliers</div>
    <svg class="act" width="16" height="16" viewBox="0 0 16 16"><circle cx="6.5" cy="6.5" r="5" stroke="#999" stroke-width="1.6" fill="none"/><path d="M10 10l5 5" stroke="#999" stroke-width="1.6"/></svg>
  </div>
  <div class="card" style="left:7px;top:76px;width:298px;height:42px">
    <div class="a val" style="left:10px;top:12px">Parts <span style="color:#888;margin-left:10px">⌄</span></div>
    <div class="a val" style="left:107px;top:12px">Represented <span style="color:#888">⌄</span></div>
    <div class="a" style="left:228px;top:7px;width:63px;height:27px;border:1px solid var(--red);border-radius:2px;color:var(--red);font-size:12px;font-weight:500;text-align:center;line-height:25px">GET</div>
  </div>
  <div class="card" style="left:7px;top:126px;width:298px;height:72px">
    <div class="a lbl" style="left:26px;top:12px;font-size:11px">Shop</div>
    <div class="a val" style="left:63px;top:10px">214 Motor Works</div>
    <div class="a lbl" style="left:14px;top:41px;font-size:11px">Contact</div>
    <div class="a" style="left:67px;top:34px;width:26px;height:26px;border-radius:50%;background:#cfcfcf"></div>
    <div class="a" style="left:102px;top:40px;font-size:12px;color:#444">Dale Fenwick</div>
  </div>
  <div class="card" style="left:7px;top:206px;width:298px;height:54px">
    <div class="chk" style="left:15px;top:20px"></div>
    <div class="a name val" style="left:45px;top:13px;font-weight:500">Norvan</div>
    <div class="a lbl" style="left:45px;top:31px;font-size:11px">Eastside Norvan</div>
    <div class="a lbl" style="right:34px;top:15px;font-size:11px">OEM Parts</div>
    <div class="a lbl" style="right:34px;top:31px;font-size:11px">▭ 29 Oct, 2019</div>
    <div class="a" style="right:12px;top:18px;color:#888">⌄</div>
  </div>
  <div class="card" style="left:7px;top:266px;width:298px;height:206px">
    <div class="chk on" style="left:15px;top:17px"><svg width="12" height="12" viewBox="0 0 12 12"><path d="M2 6l3 3 5-6" stroke="#fff" stroke-width="2" fill="none"/></svg></div>
    <div class="a val" style="left:45px;top:13px;font-weight:500">Norvan</div>
    <div class="a lbl" style="left:45px;top:29px;font-size:11px">Eastside Norvan</div>
    <div class="a lbl" style="right:45px;top:23px;font-size:11px">OEM Parts</div>
    <div class="a" style="right:12px;top:18px;color:#888">︿</div>
    <div class="a lbl" style="left:45px;top:61px">LOI</div>
    <div class="a val" style="left:45px;top:73px">5</div>
    <div class="a lbl" style="left:195px;top:61px">Disc%</div>
    <div class="a val" style="left:195px;top:73px">21</div>
    <div class="a lbl" style="left:45px;top:99px">Vol($)</div>
    <div class="a val" style="left:45px;top:112px">200</div>
    <div class="a" style="left:178px;top:108px;font-size:11px">▭ 29 Oct, 2019</div>
    <div class="a lbl" style="left:45px;top:149px">Comment</div>
    <div class="a" style="left:34px;top:165px;height:26px;padding:0 12px;border-radius:13px;background:var(--soft);font-size:13px;line-height:26px">Needed to select the supplier</div>
  </div>
  <div class="card" style="left:7px;top:482px;width:298px;height:54px">
    <div class="chk" style="left:15px;top:20px"></div>
    <div class="a val" style="left:45px;top:13px;font-weight:500">Norvan</div>
    <div class="a lbl" style="left:45px;top:31px;font-size:11px">Eastside Norvan</div>
    <div class="a lbl" style="right:34px;top:15px;font-size:11px">OEM Parts</div>
    <div class="a lbl" style="right:34px;top:31px;font-size:11px">▭ 29 Oct, 2019</div>
    <div class="a" style="right:12px;top:18px;color:#888">⌄</div>
  </div>
  <div class="card" style="left:7px;top:546px;width:298px;height:54px">
    <div class="chk" style="left:15px;top:20px"></div>
    <div class="a val" style="left:45px;top:13px;font-weight:500">Norvan</div>
    <div class="a lbl" style="left:45px;top:31px;font-size:11px">Eastside Norvan</div>
    <div class="a lbl" style="right:34px;top:15px;font-size:11px">OEM Parts</div>
    <div class="a lbl" style="right:34px;top:31px;font-size:11px">▭ 29 Oct, 2019</div>
    <div class="a" style="right:12px;top:18px;color:#888">⌄</div>
  </div>
  <div class="card" style="left:0;top:600px;width:313px;height:48px;box-shadow:0 -2px 6px rgba(0,0,0,.06)">
    <svg class="a" style="left:17px;top:16px" width="16" height="16" viewBox="0 0 16 16"><path d="M2 14l2-5 8-8 3 3-8 8z" fill="var(--red)"/></svg>
    <div class="a" style="left:54px;top:18px;font-size:11.5px;font-weight:500">COMMON COMMENT</div>
    <div class="a" style="left:186px;top:18px;font-size:11.5px;font-weight:500">SEND ACTION ALERT</div>
  </div>
</section>

</body>
</html>
```